New Business Card Design Project

Use the flyer uploaded and website www.brightoakbuilders.com for inspiration.
List Our Services on Backside of business cards
Martin Hollis
Harborline Renovations Inc.
Licensed General Contractors
858-471-9063

Contact Information for Business Card

Use the flyer uploaded and website www.brightoakbuilders.com for inspiration. List Our Services on Backside of business cards Martin Hollis Harborline Renovations Inc. Licensed General Contractors 858-471-9063

```html
<!DOCTYPE html>
<html lang="en">
<head>
<meta charset="utf-8">
<title>Harborline Renovations – Business Card</title>
<link href="https://fonts.googleapis.com/css2?family=Cinzel:wght@400;600&family=Poppins:wght@400;500;600&display=swap" rel="stylesheet">
<style>
  :root {
    --page-bg: #cbcbcb;
    --card-top: #3a3a3a;
    --card-bottom: #000000;
    --panel-dark: #111111;
    --strip-light: #3d3d3d;
    --white: #ffffff;
    --ink: #1c1c1c;
    --ink-soft: #3f3f3f;
    --text-light: #eeeeee;
    --text-muted: #bdbdbd;
    --icon-ring: #8a8a8a;
  }
  * { margin: 0; padding: 0; box-sizing: border-box; }
  html, body { width: 1200px; height: 1200px; overflow: hidden; }
  body { background: var(--page-bg); position: relative; font-family: 'Poppins', sans-serif; }

  .card {
    position: absolute; left: 172px; width: 865px; height: 495px;
    box-shadow: 0 6px 18px rgba(0,0,0,0.25); overflow: hidden;
  }

  /* Front */
  .card-front { top: 84px; background: linear-gradient(180deg, var(--card-top) 0%, #0d0d0d 55%, var(--card-bottom) 100%); }
  .front-brand {
    position: absolute; left: 0; right: 0; top: 240px; text-align: center;
    font-family: 'Cinzel', serif; font-weight: 400; font-size: 29px; letter-spacing: 0.04em;
    color: var(--text-light);
  }
  .front-web {
    position: absolute; left: 0; right: 0; top: 382px; text-align: center;
    font-family: 'Poppins', sans-serif; font-weight: 500; font-size: 20px; letter-spacing: 0.32em;
    color: var(--text-muted);
  }

  /* Back */
  .card-back { top: 622px; background: var(--white); }
  .services-panel { position: absolute; left: 0; top: 0; width: 446px; height: 495px; background: var(--panel-dark); }
  .services-strip { position: absolute; top: 0; width: 42px; height: 100%;
    background: linear-gradient(180deg, var(--strip-light) 0%, #1a1a1a 50%, #000 100%); }
  .services-strip.left { left: 0; border-right: 1px solid #6a6a6a; }
  .services-strip.right { right: 0; border-left: 1px solid #6a6a6a; }
  .services-title {
    position: absolute; left: 114px; top: 68px;
    font-family: 'Cinzel', serif; font-weight: 600; font-size: 27px; color: var(--white);
  }
  .service-list { position: absolute; left: 115px; top: 133px; list-style: none; }
  .service-item { display: flex; align-items: center; gap: 16px; height: 32px; margin-bottom: 9px;
    font-size: 17px; font-weight: 500; color: var(--text-light); line-height: 1.2; }
  .service-item.tall { height: 44px; margin-bottom: 9px; }
  .service-icon { width: 32px; height: 32px; flex: none; }

  .contact-side { position: absolute; left: 446px; top: 0; width: 419px; height: 495px; }
  .back-brand {
    position: absolute; left: 68px; top: 154px;
    font-family: 'Cinzel', serif; font-weight: 400; font-size: 19px; color: var(--ink);
  }
  .person-name {
    position: absolute; left: 68px; top: 216px;
    font-family: 'Cinzel', serif; font-weight: 600; font-size: 37px; color: var(--ink); white-space: nowrap;
  }
  .person-title { position: absolute; left: 68px; top: 263px; font-size: 16px; color: var(--ink-soft); }
  .contact-row { position: absolute; left: 68px; display: flex; align-items: center; gap: 12px;
    font-size: 17px; font-weight: 500; color: var(--ink); }
  .contact-row.phone { top: 312px; }
  .contact-row.web { top: 358px; }
  .contact-icon { width: 32px; height: 32px; flex: none; }
</style>
</head>
<body>

<section class="card card-front">
  <div class="front-brand">Harborline Renovations</div>
  <div class="front-web">www.brightoakbuilders.com</div>
</section>

<section class="card card-back">
  <div class="services-panel">
    <div class="services-strip left"></div>
    <div class="services-strip right"></div>
    <h2 class="services-title">Our Services</h2>
    <ul class="service-list">
      <li class="service-item">
        <svg class="service-icon" viewBox="0 0 32 32"><circle cx="16" cy="16" r="15" fill="#1d1d1d" stroke="var(--icon-ring)"/><rect x="10" y="9" width="12" height="5" fill="none" stroke="#ddd"/><path d="M16 14v3M16 17v7" stroke="#ddd" stroke-width="2"/></svg>
        Painting
      </li>
      <li class="service-item">
        <svg class="service-icon" viewBox="0 0 32 32"><circle cx="16" cy="16" r="15" fill="#1d1d1d" stroke="var(--icon-ring)"/><rect x="10" y="10" width="12" height="12" fill="none" stroke="#ddd"/><path d="M10 16l6-6M10 22l12-12M16 22l6-6" stroke="#ddd"/></svg>
        Flooring
      </li>
      <li class="service-item">
        <svg class="service-icon" viewBox="0 0 32 32"><circle cx="16" cy="16" r="15" fill="#1d1d1d" stroke="var(--icon-ring)"/><rect x="9" y="15" width="14" height="8" fill="none" stroke="#ddd"/><path d="M16 15v8M11 11h4v4h-4z" stroke="#ddd" fill="none"/></svg>
        Kitchens
      </li>
      <li class="service-item">
        <svg class="service-icon" viewBox="0 0 32 32"><circle cx="16" cy="16" r="15" fill="#1d1d1d" stroke="var(--icon-ring)"/><path d="M9 16h14v3a4 4 0 0 1-4 4h-6a4 4 0 0 1-4-4z M12 16V10h3" stroke="#ddd" fill="none"/></svg>
        Bathrooms
      </li>
      <li class="service-item tall">
        <svg class="service-icon" viewBox="0 0 32 32"><circle cx="16" cy="16" r="15" fill="#1d1d1d" stroke="var(--icon-ring)"/><path d="M17 8l-6 9h5l-1 7 6-9h-5z" stroke="#ddd" fill="none"/></svg>
        <span>Energy Efficienct<br>Upgrades</span>
      </li>
      <li class="service-item">
        <svg class="service-icon" viewBox="0 0 32 32"><circle cx="16" cy="16" r="15" fill="#1d1d1d" stroke="var(--icon-ring)"/><path d="M9 16l7-6 7 6M11 15v8h10v-8" stroke="#ddd" fill="none"/></svg>
        Custom Renovations
      </li>
    </ul>
  </div>

  <div class="contact-side">
    <div class="back-brand">Harborline Renovations</div>
    <div class="person-name">Martin Hollis</div>
    <div class="person-title">Licensed General Contractors</div>
    <div class="contact-row phone">
      <svg class="contact-icon" viewBox="0 0 32 32"><circle cx="16" cy="16" r="15" fill="#fff" stroke="#888"/><circle cx="16" cy="16" r="12" fill="#2a2a2a"/><path d="M12 10c-1 1-1 3 1 6s5 6 7 6l2-2-3-2-1 1c-1 0-3-2-4-4l1-1-1-3z" fill="#fff"/></svg>
      858-471-9063
    </div>
    <div class="contact-row web">
      <svg class="contact-icon" viewBox="0 0 32 32"><circle cx="16" cy="16" r="15" fill="#fff" stroke="#888"/><circle cx="16" cy="16" r="12" fill="#2a2a2a"/><circle cx="16" cy="16" r="7" fill="none" stroke="#fff"/><ellipse cx="16" cy="16" rx="3" ry="7" fill="none" stroke="#fff"/><path d="M9 16h14" stroke="#fff"/></svg>
      www.brightoakbuilders.com
    </div>
  </div>
</section>

</body>
</html>
```